Project Manager Business Card for Top Architectural Firm

Update and design a stunning Senior Project Manager Business Card

MARCO T. DRUMMOND II
Senior Project Manager

H A L C Y O N
A R C H I T E C T U R E L L C.
www.HalcyonGrandEstates.example
4127 NW 52nd Ter. Suite 2308
Miami, FL 33148
C: (305) 555-0184
mdrummond.halcyongrandestates@mailbox.example

Looking to have the logo to be UV Spot ink printed and to be prominent.

Target Market(s)

High end real estate architecture construction

Industry/Entity Type

Architect

Contact Information for Business Card

MARCO T. DRUMMOND II
Senior Project Manager

H A L C Y O N
Miami, FL 33148
C: (305) 555-0184

Font styles to use
Sans Serif

Colors

Designer to choose colors to be used in the design.

Requirements
Must have
• Prominent Logo

```html
<!DOCTYPE html>
<html lang="en">
<head>
<meta charset="utf-8">
<title>Halcyon Architecture – Business Card</title>
<link rel="stylesheet" href="https://fonts.googleapis.com/css2?family=Barlow:wght@400;500;700;800&family=Barlow+Condensed:wght@400;500;600&display=swap">
<style>
  :root {
    --backdrop: #d4d4d4;
    --card: #221f20;
    --ink: #ffffff;
    --ink-soft: #ecebeb;
    --shadow: rgba(0, 0, 0, 0.28);
  }
  * { margin: 0; padding: 0; box-sizing: border-box; }
  html, body {
    width: 1200px;
    height: 1200px;
    overflow: hidden;
    background: var(--backdrop);
  }
  .canvas {
    width: 1200px;
    height: 1200px;
    display: flex;
    align-items: center;
    justify-content: center;
    gap: 60px;
  }
  .card {
    width: 420px;
    height: 735px;
    background: var(--card);
    color: var(--ink);
    box-shadow: 0 18px 40px var(--shadow);
    display: flex;
    flex-direction: column;
    align-items: center;
  }

  /* Front */
  .card--front { justify-content: center; }
  .brand {
    display: flex;
    flex-direction: column;
    align-items: center;
    gap: 22px;
    margin-top: -20px;
  }
  .brand__mark {
    width: 96px;
    height: 96px;
    border-radius: 50%;
    background: var(--ink);
  }
  .brand__name {
    font-family: "Barlow", sans-serif;
    font-weight: 400;
    color: var(--ink);
    text-align: center;
    line-height: 1.35;
  }
  .brand__name-main {
    display: block;
    font-size: 48px;
    letter-spacing: 0.32em;
    margin-right: -0.32em;
  }
  .brand__name-sub {
    display: block;
    font-size: 15px;
    letter-spacing: 0.42em;
    margin-right: -0.42em;
  }

  /* Back */
  .card--back {
    padding: 120px 18px 0;
    text-align: center;
  }
  .person__name {
    font-family: "Barlow", sans-serif;
    font-weight: 800;
    font-size: 28px;
    letter-spacing: -0.01em;
  }
  .person__title {
    font-family: "Barlow", sans-serif;
    font-weight: 500;
    font-size: 17px;
    margin-top: 4px;
    color: var(--ink-soft);
  }
  .contact {
    list-style: none;
    margin-top: 30px;
    display: flex;
    flex-direction: column;
    align-items: center;
    gap: 28px;
  }
  .contact__item {
    display: flex;
    flex-direction: column;
    align-items: center;
    gap: 12px;
    font-family: "Barlow Condensed", sans-serif;
    font-weight: 400;
    font-size: 22px;
    line-height: 1.2;
    color: var(--ink-soft);
  }
  .contact__item--email { font-size: 20px; }
  .contact__icon { width: 44px; height: 44px; }
  .website {
    margin-top: 50px;
    font-family: "Barlow Condensed", sans-serif;
    font-weight: 600;
    font-size: 24px;
    color: var(--ink);
  }
</style>
</head>
<body>
<main class="canvas">

  <section class="card card--front" aria-label="Business card front">
    <div class="brand">
      <span class="brand__mark" aria-hidden="true"></span>
      <p class="brand__name">
        <span class="brand__name-main">HALCYON</span>
        <span class="brand__name-sub">ARCHITECTURE LLC.</span>
      </p>
    </div>
  </section>

  <section class="card card--back" aria-label="Business card back">
    <h1 class="person__name">MARCO T. DRUMMOND II</h1>
    <p class="person__title">Senior Project Manager</p>

    <ul class="contact">
      <li class="contact__item">
        <svg class="contact__icon" viewBox="0 0 44 44" aria-hidden="true">
          <rect x="8" y="8" width="28" height="28" transform="rotate(45 22 22)" fill="none" stroke="#fff" stroke-width="1.6"/>
          <rect x="17" y="15" width="10" height="14" rx="1.5" fill="#fff"/>
          <rect x="18.6" y="17" width="6.8" height="8.5" fill="#221f20"/>
        </svg>
        <span>(305) 555-0184</span>
      </li>
      <li class="contact__item contact__item--email">
        <svg class="contact__icon" viewBox="0 0 44 44" aria-hidden="true">
          <rect x="8" y="8" width="28" height="28" transform="rotate(45 22 22)" fill="none" stroke="#fff" stroke-width="1.6"/>
          <rect x="15" y="17" width="14" height="10" fill="#fff"/>
          <path d="M15 17 L22 23 L29 17" fill="none" stroke="#221f20" stroke-width="1.4"/>
        </svg>
        <span>mdrummond.halcyongrandestates@mailbox.example</span>
      </li>
      <li class="contact__item">
        <svg class="contact__icon" viewBox="0 0 44 44" aria-hidden="true">
          <rect x="8" y="8" width="28" height="28" transform="rotate(45 22 22)" fill="none" stroke="#fff" stroke-width="1.6"/>
          <path d="M22 30 C18 25 16.5 22.5 16.5 20 A5.5 5.5 0 0 1 27.5 20 C27.5 22.5 26 25 22 30 Z" fill="#fff"/>
          <circle cx="22" cy="20" r="2" fill="#221f20"/>
        </svg>
        <span>4127 NW 52nd Ter. Suite 2308<br>Miami, FL 33148</span>
      </li>
    </ul>

    <p class="website">www.HalcyonGrandEstates.example</p>
  </section>

</main>
</body>
</html>
```